Calvanta Group Real Estate Company business cards

New business card design, we are generally happy with the basic layout of the existing front of business card, (feel free to change) but require a head shot photo on the back side.

http://www.calvanta.com.au/

Attached logos, and existing business card

------------------------------

Target Market(s)

Real estate

Industry/Entity Type

Real Estate

Contact Information for Business Card

Standard size double sided

Font styles to use
Other font styles liked:
• Futura

Requirements
Must have
• Photo head shot on the back side
Nice to have
• yes
Should not have
• No

```html
<!DOCTYPE html>
<html lang="en">
<head>
<meta charset="utf-8">
<title>Calvanta Group Business Cards</title>
<link href="https://fonts.googleapis.com/css2?family=Jost:wght@400;500;600&family=Roboto:wght@400;500&display=swap" rel="stylesheet">
<style>
  :root {
    --bg: #e4e4e4;
    --card: #ffffff;
    --purple: #2b1b4f;
    --orange: #f07c14;
    --rule: #b9b9b9;
    --photo-light: #eef0f4;
    --photo-dark: #2c3d5f;
  }
  * { box-sizing: border-box; margin: 0; padding: 0; }
  html, body { width: 1200px; height: 1200px; overflow: hidden; }
  body { background: var(--bg); font-family: "Roboto", sans-serif; position: relative; }

  .card {
    position: absolute; left: 162px; width: 875px; height: 500px;
    background: var(--card); border-radius: 28px; overflow: hidden;
    box-shadow: 0 6px 18px rgba(0,0,0,0.12);
  }
  /* Back side carries the head shot, shown on top; front side carries contacts */
  .card-back { top: 60px; }
  .card-front { top: 640px; }

  .tagline {
    position: absolute; left: 70px; top: 150px;
    font-family: "Jost", sans-serif; font-weight: 400; font-size: 46px; line-height: 1.08;
    color: var(--purple);
  }
  .tagline .accent { color: var(--orange); }

  .brand-name {
    position: absolute; font-family: "Jost", sans-serif; font-weight: 500;
    color: var(--purple); letter-spacing: -1px; white-space: nowrap;
  }
  .card-back .brand-name { left: 70px; top: 360px; font-size: 66px; }
  .card-front .brand-name { left: 70px; top: 140px; font-size: 76px; }

  .headshot {
    position: absolute; right: 0; top: 0; width: 330px; bottom: 0;
    background: linear-gradient(180deg, var(--photo-light) 0%, #d3d8e2 40%, var(--photo-dark) 100%);
  }

  .person { position: absolute; right: 80px; top: 95px; text-align: right; }
  .person-name { font-family: "Jost", sans-serif; font-weight: 600; font-size: 30px; color: var(--purple); }
  .person-role { font-size: 16px; color: #555; margin-top: 2px; }

  .divider { position: absolute; left: 70px; right: 80px; top: 255px; height: 1px; background: var(--rule); }

  .social { position: absolute; right: 80px; top: 275px; display: flex; align-items: center; gap: 6px; font-size: 17px; color: var(--purple); }
  .social .label { margin-right: 6px; }
  .social .dot { width: 20px; height: 20px; background: var(--orange); border-radius: 3px; }
  .abn { position: absolute; right: 80px; top: 315px; font-size: 17px; color: var(--purple); }

  .contacts { position: absolute; left: 150px; top: 340px; width: 340px; border-top: 1px solid var(--rule); padding-top: 12px; }
  .contact { display: flex; align-items: center; gap: 14px; font-size: 19px; color: var(--purple); height: 28px; }
  .contact svg { width: 18px; height: 18px; flex: none; }

  .bands { position: absolute; left: 0; bottom: 0; width: 875px; height: 100px; }
</style>
</head>
<body>

<section class="card card-back" aria-label="Back side">
  <p class="tagline">Let us<br>show you<br><span class="accent">property</span></p>
  <div class="brand-name">calvanta group</div>
  <div class="headshot" role="img" aria-label="Head shot photo of the director in a navy suit and blue tie"></div>
</section>

<section class="card card-front" aria-label="Front side">
  <div class="brand-name">calvanta group</div>

  <div class="person">
    <div class="person-name">Daniel Tran</div>
    <div class="person-role">Director</div>
  </div>

  <div class="divider"></div>

  <div class="social">
    <span class="label">Find us:</span>
    <span class="dot"></span><span class="dot"></span><span class="dot"></span>
  </div>
  <div class="abn">ABN: 12 345 678 901</div>

  <div class="contacts">
    <div class="contact">
      <svg viewBox="0 0 18 18"><rect x="4" y="1" width="10" height="16" rx="2" fill="var(--orange)"/><rect x="6" y="3.5" width="6" height="9" fill="#fff"/></svg>
      <span>0400 555 018</span>
    </div>
    <div class="contact">
      <svg viewBox="0 0 18 18" fill="none" stroke="var(--orange)" stroke-width="1.8"><circle cx="9" cy="9" r="7.5"/><ellipse cx="9" cy="9" rx="3.2" ry="7.5"/><line x1="1.5" y1="9" x2="16.5" y2="9"/></svg>
      <span>www.calvanta.com.au</span>
    </div>
    <div class="contact">
      <svg viewBox="0 0 18 18"><rect x="1" y="3.5" width="16" height="11" rx="1" fill="var(--orange)"/><polyline points="1.5,4.5 9,10 16.5,4.5" fill="none" stroke="#fff" stroke-width="1.5"/></svg>
      <span>daniel.tran@calvanta.com.au</span>
    </div>
  </div>

  <svg class="bands" viewBox="0 0 875 100" preserveAspectRatio="none">
    <polygon points="0,84 540,54 565,100 0,100" fill="var(--orange)"/>
    <polygon points="540,20 875,20 875,100 575,100" fill="var(--purple)"/>
  </svg>
</section>

</body>
</html>
```